Flyer Handout when attending Dental Conventions, or dental office shows

take the sample file folder that is shown with 2 pictures. The outside and inside of the folder needs to be completed, along with the inserts. This folder pictures are from someone elses flyer/folder and i would like to have it layout like this. The KPW inserts is informational, but it is lacking originality, pictures, etc. Try to make our information and move it to 2017. When this is done, i would like to take this flyer and load it to the web or allow to send via email and make it interactive. The user can select the flyers and it will slide or flip to the flyer. this will make if kewl/fun

Target Market(s)

Dental Offices

Industry/Entity Type

Dental

Font styles to use
Serif
Sans Serif

Colors

Designer to choose colors to be used in the design.

Requirements
Must have
• a Semi new look and feel of our flyers, and a new envelope created

```html
<!DOCTYPE html>
<html lang="en">
<head>
<meta charset="utf-8">
<title>KPW Folder Inserts – Inner Spreads</title>
<link href="https://fonts.googleapis.com/css2?family=Montserrat:wght@400;500;600;700&display=swap" rel="stylesheet">
<style>
  :root{
    --stage:#1f1e24;
    --white:#ffffff;
    --orange:#f7973a;
    --blue:#0e6d9e;
    --ink:#2b2b2b;
    --photo-clinic:linear-gradient(135deg,#f3f5f8 0%,#dfe6ee 45%,#9fb6cc 100%);
    --photo-doctor:linear-gradient(180deg,#f4f6f8 0%,#e3e8ee 60%,#c9d3de 100%);
    --photo-room:linear-gradient(135deg,#f6f8fa 0%,#dde5ea 55%,#4fa79c 100%);
    --photo-tools:linear-gradient(135deg,#0f3e74 0%,#3e78b8 50%,#a9c7e6 100%);
  }
  *{box-sizing:border-box;margin:0;padding:0}
  html,body{width:1200px;height:1200px;overflow:hidden;background:var(--stage)}
  body{font-family:"Montserrat",Arial,sans-serif;color:var(--ink)}
  .canvas{position:relative;width:1200px;height:1200px}
  .spread-label{position:absolute;top:128px;font-size:48px;font-weight:600;color:var(--white);letter-spacing:0.5px}
  .page{position:absolute;top:210px;width:552px;height:781px;background:var(--white);overflow:hidden}
  .page--one{left:42px}
  .page--two{left:594px;width:554px}
  .block{position:absolute;left:0;right:0}
  .band-blue{background:var(--blue);color:var(--white)}
  .footer-cta{position:absolute;left:0;right:0;bottom:0;height:63px;background:var(--orange);color:var(--white);
    display:flex;align-items:center;justify-content:center;font-size:15.5px;font-weight:600}
  .photo{position:absolute}
  .heading{color:var(--orange);font-weight:600;font-size:20px;line-height:1.2}
  .body-copy{font-size:9.5px;line-height:12.8px}
  .body-copy p+p{margin-top:12px}
  .tick-list{list-style:none}
  .tick-list li{position:relative;padding-left:16px;font-size:9.5px;line-height:11.5px;margin-bottom:13px}
  .tick-list svg{position:absolute;left:0;top:1px;width:10px;height:10px}
</style>
</head>
<body>
<div class="canvas">
  <div class="spread-label" style="left:48px">Inner 1</div>
  <div class="spread-label" style="left:600px">Inner 2</div>

  <section class="page page--one">
    <div class="photo" style="left:0;top:0;width:552px;height:284px;background:var(--photo-clinic)" role="img" aria-label="Photo of a dentist examining a smiling patient's teeth"></div>

    <div class="block band-blue" style="top:284px;height:196px;padding:22px 26px 0 28px">
      <h2 class="heading" style="margin-bottom:12px">We are proud to announce a NEW feature.</h2>
      <div class="body-copy">
        <p>You are now able to process real-time eligibility. This service is an easy-to-use solution providing instant connectivity to leading commercial and government insurers. This service will help you to automate time-consuming business functions while improving patient services.</p>
        <p>KPW real-time eligibility consolidates access to multiple payers from a single screen with the one source solution, it allows dental offices to receive eligibility and plan benefit information immediately from insurance companies. Most importantly, the eligibility information received is displayed in an understandable, easy to read format that can be printed and shared with your patient.</p>
      </div>
    </div>

    <div class="photo" style="left:0;top:480px;width:216px;height:238px;background:var(--photo-doctor)" role="img" aria-label="Photo of a smiling dentist in a white coat giving a thumbs up"></div>
    <div class="block" style="top:512px;left:250px;right:26px">
      <h3 class="heading" style="margin-bottom:12px">Benefits:</h3>
      <ul class="tick-list">
        <li><svg viewBox="0 0 12 12"><path d="M1.5 6.5l3 3 6-7" fill="none" stroke="#f7973a" stroke-width="2"/></svg>Decrease the amount of phone calls to insurance companies.</li>
        <li><svg viewBox="0 0 12 12"><path d="M1.5 6.5l3 3 6-7" fill="none" stroke="#f7973a" stroke-width="2"/></svg>Improve your patient services by knowing at the time of service what is owed.</li>
        <li><svg viewBox="0 0 12 12"><path d="M1.5 6.5l3 3 6-7" fill="none" stroke="#f7973a" stroke-width="2"/></svg>Expedite reimbursements.</li>
        <li><svg viewBox="0 0 12 12"><path d="M1.5 6.5l3 3 6-7" fill="none" stroke="#f7973a" stroke-width="2"/></svg>Increase cash flow.</li>
        <li><svg viewBox="0 0 12 12"><path d="M1.5 6.5l3 3 6-7" fill="none" stroke="#f7973a" stroke-width="2"/></svg>Improve dental claims acceptance rates.</li>
      </ul>
    </div>

    <div class="footer-cta">Call us Today at (800) 555-0142</div>
  </section>

  <section class="page page--two">
    <div class="block" style="top:0;height:137px;padding:22px 26px 0 26px">
      <h2 class="heading" style="margin-bottom:10px">Implementation:</h2>
      <p class="body-copy">Please contact KPW support and we will activate your eligibility service within the KPW Bridge and the KPW Portal within minutes.</p>
      <p class="heading" style="font-size:15px;margin-top:18px">At KPW we are proud to announce a NEW feature for offices.</p>
    </div>

    <div class="block band-blue" style="top:137px;height:180px;padding:16px 26px 0 28px">
      <h2 class="heading" style="color:var(--white);margin-bottom:10px">KPW Auto-Post:</h2>
      <div class="body-copy">
        <p>Payment posting that accelerates the revenue cycle by automatically posting payments for virtually any payer that provides electronic EOB's. If you are receiving your EOB's on the KPW Portal or would like to receive, you can now post them directly into your Dental Software Package.</p>
        <p>Our expert staff will work closely with each client to create a customized Auto Post solution in the KPW Bridge that will interface with your Dental Software Package. Auto-Post will post primary and secondary claims, contractual adjustments, rejection notes, and claims status notes. The results of this combination are very significant and will benefit your office and increase efficiency.</p>
      </div>
    </div>

    <div class="photo" style="left:0;top:338px;width:234px;height:166px;background:var(--photo-room)" role="img" aria-label="Photo of a bright modern dental treatment room with a teal chair"></div>
    <div class="block" style="top:336px;left:250px;right:18px">
      <h3 class="heading" style="margin-bottom:10px">Features:</h3>
      <ul class="tick-list">
        <li><svg viewBox="0 0 12 12"><path d="M1.5 6.5l3 3 6-7" fill="none" stroke="#f7973a" stroke-width="2"/></svg>Automated payment posting for participating Government and Commercial payers</li>
        <li><svg viewBox="0 0 12 12"><path d="M1.5 6.5l3 3 6-7" fill="none" stroke="#f7973a" stroke-width="2"/></svg>Robust decision support.</li>
        <li><svg viewBox="0 0 12 12"><path d="M1.5 6.5l3 3 6-7" fill="none" stroke="#f7973a" stroke-width="2"/></svg>Tailored error and exception rules.</li>
        <li><svg viewBox="0 0 12 12"><path d="M1.5 6.5l3 3 6-7" fill="none" stroke="#f7973a" stroke-width="2"/></svg>Customized solutions that work with any existing</li>
        <li><svg viewBox="0 0 12 12"><path d="M1.5 6.5l3 3 6-7" fill="none" stroke="#f7973a" stroke-width="2"/></svg>Easy integration</li>
      </ul>
    </div>

    <div class="block" style="top:522px;left:26px;width:280px">
      <h3 class="heading" style="margin-bottom:10px">Benefits:</h3>
      <ul class="tick-list">
        <li><svg viewBox="0 0 12 12"><path d="M1.5 6.5l3 3 6-7" fill="none" stroke="#f7973a" stroke-width="2"/></svg>Detailed reporting every step of the way</li>
        <li><svg viewBox="0 0 12 12"><path d="M1.5 6.5l3 3 6-7" fill="none" stroke="#f7973a" stroke-width="2"/></svg>Elimination of manual data entry</li>
        <li><svg viewBox="0 0 12 12"><path d="M1.5 6.5l3 3 6-7" fill="none" stroke="#f7973a" stroke-width="2"/></svg>Automation that saves time and reduces errors</li>
        <li><svg viewBox="0 0 12 12"><path d="M1.5 6.5l3 3 6-7" fill="none" stroke="#f7973a" stroke-width="2"/></svg>Fast identification of claim discrepancies</li>
        <li><svg viewBox="0 0 12 12"><path d="M1.5 6.5l3 3 6-7" fill="none" stroke="#f7973a" stroke-width="2"/></svg>Customizable solutions that fit any provider's business needs</li>
      </ul>
    </div>
    <div class="photo" style="left:314px;top:526px;width:240px;height:164px;background:var(--photo-tools)" role="img" aria-label="Photo of dental mirror and instruments on a blue-lit tray"></div>

    <div class="footer-cta">Call us Today at (800) 555-0142</div>
  </section>
</div>
</body>
</html>
```